New Menu Design Project

Golden Griddle & Morning Kitchen is a Canadian Franchise Chain that currently has 60+ locations. We are looking for our menu to be modernized and redesigned to keep ahead of current trends
Attached you will find our current menu with photos from our various photoshoots, please use as per needed on the menu as we have some great shots of our products that we would like to showcase, especially our pancakes, waffles, French toast & crepes
Additionally you will find a Sample Menu of what we were thinking but we would like to see what other modern menu designs/creative freedom you can come up with
Please remove all beverages from this menu
Please see below link for all files: https://files.brivoshare.net/folders/7K42pqzwexRtaMbn3VdLsY9oHcF1jA5?usp=share_link

```html
<!DOCTYPE html>
<html lang="en">
<head>
<meta charset="utf-8">
<title>Breakfast Menu Spread</title>
<link rel="stylesheet" href="https://fonts.googleapis.com/css2?family=Poppins:ital,wght@0,400;0,600;0,700;0,800;1,400&family=Oswald:wght@500;600&family=Great+Vibes&display=swap">
<style>
:root{
  --backdrop:#f6d80c;
  --wood-dark:#1f130d;
  --wood-mid:#3a261a;
  --wood-light:#4a3222;
  --gold:#f4c20d;
  --gold-deep:#c99a0a;
  --maroon:#7a1b16;
  --maroon-dark:#5a1410;
  --cream:#fff6e2;
  --white:#ffffff;
  --panel:rgba(90,70,55,.78);
  --cal-band:rgba(170,132,16,.85);
}
*{box-sizing:border-box;margin:0;padding:0}
html,body{width:1200px;height:952px;overflow:hidden}
body{background:var(--backdrop);font-family:"Poppins",sans-serif;color:var(--white);position:relative}
.spread{position:absolute;left:40px;top:101px;width:1120px;height:750px;display:flex;box-shadow:0 18px 40px rgba(0,0,0,.35)}
.page{position:relative;width:560px;height:750px;overflow:hidden;
  background:linear-gradient(90deg,var(--wood-dark),var(--wood-mid) 35%,var(--wood-light) 55%,var(--wood-mid) 80%,var(--wood-dark))}
.page--left{border-right:1px solid rgba(0,0,0,.5)}
.page--right{border-left:1px solid rgba(255,255,255,.06)}

/* section header */
.section-tag{position:absolute;z-index:3;left:32px;top:10px;width:148px;height:60px;background:var(--gold);
  display:flex;align-items:center;justify-content:center;font-weight:800;font-size:27px;color:var(--maroon);letter-spacing:-.5px}
.special{position:absolute;z-index:3;left:200px;top:12px;width:190px;height:58px;background:var(--maroon);padding:6px 8px}
.special__title{font-weight:700;color:var(--gold);font-size:15px;line-height:1}
.special__price{position:absolute;right:8px;top:6px;font-weight:700;font-size:17px;color:var(--gold)}
.special__script{position:absolute;left:70px;top:18px;font-family:"Great Vibes",cursive;font-size:27px;color:var(--white);line-height:1}
.special__hours{position:absolute;left:8px;top:28px;font-size:6px;line-height:1.5;color:var(--cream)}

/* food photos */
.photo{position:absolute;z-index:1;border-radius:50%;
  background:radial-gradient(ellipse at 50% 50%,#d99a3c 0,#c2772c 38%,#f4efe6 58%,#ffffff 70%,#e6e2dc 100%);
  box-shadow:0 4px 10px rgba(0,0,0,.45)}
.photo--side{background:radial-gradient(ellipse at 55% 50%,#b4713a 0,#8e5a30 40%,#f2eee8 62%,#ffffff 80%,#ddd 100%)}
.photo--basket{border-radius:14px;background:radial-gradient(ellipse at 50% 55%,#d7913f 0,#e8c27a 40%,#eef0f2 70%,#d9dde0 100%)}

/* menu entries */
.entry{position:absolute;z-index:3;background:var(--panel);padding:5px 8px 6px}
.entry__head{display:flex;justify-content:space-between;align-items:baseline;gap:10px}
.entry__name{font-weight:700;font-size:11.5px;line-height:1.2;white-space:nowrap}
.entry__name span{border-bottom:2px solid var(--gold)}
.entry__price{font-weight:700;font-size:11.5px}
.entry__desc{font-style:italic;font-size:6.4px;line-height:1.45;margin-top:3px;color:var(--cream)}
.entry--right .entry__desc{text-align:right}
.cal{position:absolute;z-index:4;background:var(--cal-band);padding:2px 10px;font-style:italic;font-size:7.5px;color:var(--gold);white-space:nowrap}

/* footers */
.footer{position:absolute;z-index:3;bottom:25px;height:30px;display:flex;align-items:center}
.footer--left{left:248px;right:0}
.sig{height:100%;width:80px;background:var(--maroon);display:flex;align-items:center;gap:5px;padding-left:14px;
  font-family:"Oswald",sans-serif;font-size:6.5px;line-height:1.1;text-transform:uppercase}
.flavour{flex:1;height:100%;background:var(--gold-deep);display:flex;align-items:center;gap:6px;padding-left:10px;
  font-family:"Oswald",sans-serif;font-size:6.5px;line-height:1.15;text-transform:uppercase}
.flavour em{font-style:normal;color:var(--gold)}
.footer--right{left:0;right:0}
.spice{width:190px;height:100%;background:var(--gold-deep);display:flex;align-items:center;gap:6px;padding-left:30px;
  font-family:"Oswald",sans-serif;font-size:6.5px;line-height:1.15;text-transform:uppercase}
.notice{flex:1;height:100%;background:var(--maroon-dark);display:flex;align-items:center;padding:0 10px;
  font-style:italic;font-size:5.2px;line-height:1.6;color:var(--cream)}
</style>
</head>
<body>
<main class="spread">
  <section class="page page--left">
    <div class="section-tag">Breakfast</div>
    <div class="special">
      <div class="special__title">Breakfast</div>
      <div class="special__script">Special</div>
      <div class="special__price">$6.99</div>
      <div class="special__hours">MON - FRI<br>7AM - 9AM</div>
    </div>

    <div class="photo" style="left:262px;top:72px;width:200px;height:100px" role="img" aria-label="Plate with homefries, two sunny-side eggs and bacon"></div>
    <div class="photo photo--side" style="left:398px;top:10px;width:80px;height:42px" role="img" aria-label="Side plate of Texas toast with jam cup"></div>
    <div class="entry" style="left:80px;top:80px;width:178px">
      <div class="entry__head"><div class="entry__name"><span>EXP</span>RESS</div><div class="entry__price">$10.79</div></div>
      <p class="entry__desc">2 eggs, choice of bacon, ham, or sausage, served with homefries and Texas toast. Substitute peameal or turkey bacon, add $1.00.</p>
    </div>
    <div class="cal" style="left:160px;top:140px">Calories: 710 - 950 Cals</div>

    <div class="photo photo--side" style="left:30px;top:140px;width:80px;height:42px" role="img" aria-label="Side plate of Texas toast with jam cup"></div>
    <div class="photo" style="left:52px;top:178px;width:205px;height:100px" role="img" aria-label="Plate with ham, eggs and homefries"></div>
    <div class="entry entry--right" style="left:268px;top:178px;width:180px">
      <div class="entry__head"><div class="entry__name"><span>Jumbo</span> EXPRESS</div><div class="entry__price">$12.79</div></div>
      <p class="entry__desc">3 eggs, choice of bacon, ham, or sausage. Served with homefries and Texas toast. Substitute peameal or turkey bacon, add $1.00.</p>
    </div>
    <div class="cal" style="left:262px;top:238px">Calories: 840 - 1220 Cals</div>
    <div class="photo photo--side" style="left:460px;top:222px;width:80px;height:40px" role="img" aria-label="Side plate of Texas toast with jam cup"></div>

    <div class="photo" style="left:275px;top:268px;width:200px;height:100px" role="img" aria-label="Plate with homefries, eggs and sliced tomato"></div>
    <div class="entry" style="left:71px;top:292px;width:196px">
      <div class="entry__head"><div class="entry__name"><span>EXPRESS</span> No-Meat</div><div class="entry__price">$9.29</div></div>
      <p class="entry__desc">2 eggs served with homefries and Texas toast.</p>
    </div>
    <div class="cal" style="left:170px;top:328px">Calories: 620 Cals</div>

    <div class="photo" style="left:58px;top:370px;width:200px;height:108px" role="img" aria-label="Plate with farmers sausage, eggs and homefries"></div>
    <div class="entry entry--right" style="left:267px;top:380px;width:212px">
      <div class="entry__head"><div class="entry__name"><span>Farmers</span> Sausage &amp; Eggs</div><div class="entry__price">$13.79</div></div>
      <p class="entry__desc">2 eggs with butterflied farmers sausage and fried onions. Served with homefries and Texas toast.</p>
    </div>
    <div class="cal" style="left:267px;top:428px">Calories: 1330 Cals</div>

    <div class="photo photo--side" style="left:440px;top:436px;width:80px;height:40px" role="img" aria-label="Side plate of Texas toast with jam cup"></div>
    <div class="photo" style="left:288px;top:472px;width:200px;height:104px" role="img" aria-label="Plate with bacon, sausage, ham, eggs and homefries"></div>
    <div class="entry" style="left:84px;top:492px;width:196px">
      <div class="entry__head"><div class="entry__name"><span>The</span> Meatlovers</div><div class="entry__price">$15.90</div></div>
      <p class="entry__desc">3 eggs with bacon, ham, and sausage. Served with homefries and Texas toast.</p>
    </div>
    <div class="cal" style="left:180px;top:530px">Calories: 1230 Cals</div>

    <div class="photo" style="left:70px;top:585px;width:200px;height:110px" role="img" aria-label="Plate with striploin steak, scrambled eggs and homefries"></div>
    <div class="entry entry--right" style="left:279px;top:598px;width:185px">
      <div class="entry__head"><div class="entry__name"><span>Steak</span> n'Eggs</div><div class="entry__price">$19.99</div></div>
      <p class="entry__desc">6 oz. New York Striploin with 3 eggs, homefries, and Texas toast.</p>
    </div>
    <div class="cal" style="left:279px;top:645px">Calories: 1040 Cals</div>

    <div class="footer footer--left">
      <div class="sig">
        <svg width="14" height="12" viewBox="0 0 14 12" aria-hidden="true"><g fill="none" stroke="#fff" stroke-width="1.2"><ellipse cx="7" cy="3" rx="6" ry="2"/><path d="M1 6c0 1 3 2 6 2s6-1 6-2M1 9c0 1 3 2 6 2s6-1 6-2"/></g></svg>
        <span>Signature<br>Item</span>
      </div>
      <div class="flavour">
        <svg width="13" height="13" viewBox="0 0 24 24" aria-hidden="true"><path fill="#fff" d="M12 1l3.2 7 7.6.8-5.7 5.1 1.6 7.5L12 17.6 5.3 21.4l1.6-7.5L1.2 8.8 8.8 8z"/></svg>
        <span>Flavour your stack to any of the options under<br><em>"Signature Stacks"</em> for $1.99 (235 - 1000 Cals)</span>
      </div>
    </div>
  </section>

  <section class="page page--right">
    <div class="photo photo--side" style="left:400px;top:8px;width:80px;height:40px" role="img" aria-label="Side plate of Texas toast with jam cup"></div>
    <div class="photo" style="left:272px;top:48px;width:205px;height:100px" role="img" aria-label="Plate with pancake, bacon, sausage, eggs and homefries"></div>
    <div class="entry" style="left:62px;top:62px;width:200px">
      <div class="entry__head"><div class="entry__name"><span>Junior</span> Stack</div><div class="entry__price">$12.79</div></div>
      <p class="entry__desc">2 eggs served with 1 bacon, 1 sausage, 1 pancake, homefries and Texas Toast. Substitute peameal or turkey bacon, add $1.00.</p>
    </div>
    <div class="cal" style="left:155px;top:115px">Calories: 1030 Cals</div>

    <div class="photo photo--basket" style="left:8px;top:150px;width:200px;height:150px" role="img" aria-label="Breakfast wrap with homefries in a paper-lined basket"></div>
    <div class="entry entry--right" style="left:220px;top:182px;width:178px">
      <div class="entry__head"><div class="entry__name"><span>Breakfast</span> Wrap</div><div class="entry__price">$14.69</div></div>
      <p class="entry__desc">3 eggs with your choice of 4 toppings: onions, green peppers, tomatoes, mushrooms, jalapeños, spinach, guacamole, pico salsa, bacon, ham, sausage, cheddar, feta, mozza, BBQ sauce. Served with homefries.</p>
    </div>
    <div class="cal" style="left:220px;top:256px">Calories: 850 Cals</div>

    <div class="photo photo--side" style="left:412px;top:234px;width:80px;height:40px" role="img" aria-label="Side plate of Texas toast with jam cup"></div>
    <div class="photo" style="left:282px;top:278px;width:200px;height:100px" role="img" aria-label="Plate with pancakes, eggs and homefries"></div>
    <div class="entry" style="left:105px;top:307px;width:165px">
      <div class="entry__head"><div class="entry__name"><span>Steak</span> n' Eggs</div><div class="entry__price">$19.99</div></div>
      <p class="entry__desc">6 oz. New York Striploin with 3 eggs, homefries and Texas toast.</p>
    </div>
    <div class="cal" style="left:175px;top:347px">Calories: 1040 Cals</div>

    <div class="photo" style="left:55px;top:386px;width:195px;height:104px" role="img" aria-label="Plate with waffles, bacon, sausage, eggs and homefries"></div>
    <div class="entry" style="left:268px;top:398px;width:175px">
      <div class="entry__head"><div class="entry__name"><span>Waffle</span> Stack</div><div class="entry__price">$16.79</div></div>
      <p class="entry__desc">2 eggs served with 2 bacon, 2 sausage, 2 maple infused waffles and homefries.</p>
    </div>
    <div class="cal" style="left:268px;top:440px">Calories: 1460 Cals</div>

    <div class="photo" style="left:295px;top:474px;width:195px;height:104px" role="img" aria-label="Plate with pancakes, eggs, bacon and sausage"></div>
    <div class="entry" style="left:90px;top:507px;width:165px">
      <div class="entry__head"><div class="entry__name"><span>Pancake</span> Stack</div><div class="entry__price">$15.79</div></div>
      <p class="entry__desc">2 eggs served with 2 bacon, 2 sausage, 2 pancakes and homefries.</p>
    </div>
    <div class="cal" style="left:175px;top:550px">Calories: 1130 Cals</div>

    <div class="photo" style="left:80px;top:588px;width:200px;height:106px" role="img" aria-label="Plate with French toast, sausage, bacon, eggs and homefries"></div>
    <div class="entry entry--right" style="left:300px;top:602px;width:195px">
      <div class="entry__head"><div class="entry__name"><span>French</span> Toast Stack</div><div class="entry__price">$16.79</div></div>
      <p class="entry__desc">2 eggs served with 2 bacon, 2 sausage, 2 pieces of french toast and homefries.</p>
    </div>
    <div class="cal" style="left:300px;top:645px">Calories: 1020 Cals</div>

    <div class="footer footer--right">
      <div class="spice">
        <svg width="12" height="14" viewBox="0 0 12 14" aria-hidden="true"><path d="M6 1c2 2 4 5 1 9-2 2-5 3-5 3 1-3 0-6 2-8" fill="none" stroke="#fff" stroke-width="1.2"/></svg>
        <span>Spice up your homefries with sautéed onions,<br>peppers and jalapeños for $1.99 (150 Cals)</span>
      </div>
      <p class="notice">Adults and youth (ages 13 and older) need an average of 2,000 calories a day, and children (ages 4 to 12) need an average of 1,500 calories a day. However, individual needs vary.</p>
    </div>
  </section>
</main>
</body>
</html>
```